Professional services

we are preparing a flyer for an event to promote our new service. to use organge colour as background ( our corporate colour)

Header : Social Media Monitoring, Analytics and Engagement
text :
Leveraging on best of bred technologies, domain knowledge and oversea delivery centres, Vantrelle provides social media monitoring, analytic and engagement services.

This can be used for branding, online reputation, social CRM (sales, marketing & customer services), planning & measurement of campaign and research.

Please contact us at contactus@vantrelle-example.biz to explore more.

Industry/Entity Type

Marketing

```html
<!DOCTYPE html>
<html lang="en">
<head>
<meta charset="utf-8">
<title>Vantrelle — Social Media Monitoring, Analytics &amp; Engagement</title>
<link href="https://fonts.googleapis.com/css2?family=Oxanium:wght@400&family=Libre+Franklin:wght@400;500&display=swap" rel="stylesheet">
<style>
  :root {
    --page-bg: #ffffff;
    --orange-deep: #ff5a00;
    --orange-mid: #ff8a1e;
    --orange-light: #ffc27a;
    --glow: #fff0dc;
    --gold: #ffd780;
    --ink: #000000;
  }
  * { margin: 0; padding: 0; box-sizing: border-box; }
  html, body {
    width: 1200px; height: 1000px; overflow: hidden;
    background: var(--page-bg);
  }
  .flyer {
    position: absolute; left: 380px; top: 16px;
    width: 455px; height: 964px; overflow: hidden;
  }
  .flyer__backdrop {
    position: absolute; inset: 0;
    background:
      radial-gradient(ellipse 180px 110px at 50% 9%, rgba(255,215,128,0.85), rgba(255,215,128,0) 100%),
      radial-gradient(ellipse 300px 360px at 46% 42%, var(--glow) 0%, var(--orange-light) 50%, rgba(255,194,122,0) 100%),
      linear-gradient(180deg, var(--orange-mid) 0%, var(--orange-mid) 62%, var(--orange-deep) 100%);
  }
  .flyer__headline {
    position: absolute; left: 33px; top: 200px; width: 420px;
    font-family: "Oxanium", sans-serif; font-weight: 400;
    font-size: 66px; line-height: 84px; color: var(--ink);
    letter-spacing: 1.5px;
  }
  .flyer__body {
    position: absolute; left: 31px; top: 586px; width: 399px;
    font-family: "Libre Franklin", sans-serif; font-size: 16.5px;
    line-height: 23px; color: var(--ink);
    text-align: justify; hyphens: manual;
  }
  .flyer__body p + p { margin-top: 30px; }
  .flyer__contact {
    position: absolute; left: 0; top: 890px; width: 455px;
    text-align: center; font-family: "Libre Franklin", sans-serif;
    font-size: 16px; line-height: 24px; color: var(--ink);
  }
  .flyer__email { font-weight: 500; }
</style>
</head>
<body>
  <main class="flyer">
    <div class="flyer__backdrop" role="img" aria-label="Warm orange background with glowing bokeh light circles along the top and soft light streaks"></div>

    <h1 class="flyer__headline">Social Media Monitoring, Analytics &amp; Engagement</h1>

    <section class="flyer__body">
      <p>Leveraging on best of bred technologies, domain knowledge and oversea delivery centres, Van&shy;trelle provides social media monitoring, analytic and engagement services.</p>
      <p>This can be used for branding, online reputation, social CRM (sales, marketing &amp; customer ser&shy;vices), planning &amp; measurement of campaign and research.</p>
    </section>

    <footer class="flyer__contact">
      Please contact us<br>
      <span class="flyer__email">contactus@vantrelle-example.biz</span> to explore more
    </footer>
  </main>
</body>
</html>
```